Plakat-Design für Immobilien
Sehr kompetent, schnelle Reaktionszeit und verlässlich. Die Kommunikation war sehr angenehm und alle Wünsche wurden rasch umgesetzt. Gerne wieder!
Zielgruppe
Mein Unternehmen heißt KO.RV Immobilien & Design e.U. und ist mit der Vermittlung von Immobilien betraut. Überwiegend handelt es sich hierbei um Neubauprojekte von Bauträgern, welche in einem sehr modernen Stil gehalten sind. Wir suchen ständig nach Personen, die Ihre Immobilie verkaufen möchten und die wir dabei unterstützen können.
Aufgabenstellung
Wir benötigen ein Plakat auf der Hauptstraße mit den Maßen 4900 mm x 2300 mm, welches von vielen Autofahrern sofort gesehen wird und auch im Gedächtnis bleiben soll. Die Zielgruppe sind Personen/Autofahrer jeden Alters, die ihre Immobilie verkaufen möchten und einen erfahrenen Immobilienmakler zur Vermarktung suchen. Ein Beispielfoto einer Plakatwerbung befindet sich im Anhang.
Wichtig ist, dass die Botschaft rüber kommt, dass wir 'das Immobilienbüro in der Region' sind. Also Regionalität ist sehr wichtig, da die Zielgruppe ebenfalls aus der selben Region kommt.
Es soll ein Bild von mir (siehe Anhang) zu sehen sein und evtl. ein oder mehrere Bilder von Häusern (Professionelle Stockfotos).
Weiters soll ein Spruch stehen wie bspw.
-) Verkaufen Sie besser mit uns
-) Wir verkaufen Ihre Immobilie
-) Legen Sie Ihre Immobilie in gute Hände
-) Ihr regionaler Immobilien-Experte
-) Heimvorteil - Ihr Immobilienmakler aus der Region
-) Immobilie verkaufen? Wir machen Ihre Hausaufgaben!
Wir sind offen für kreative Ideen bezgl. Spruch - bitte eigene Ideen mit einbringen.
Weiters soll das Logo und Kontaktdaten (mindestens Telefonnummer und Website) zu sehen sein.
Weiters können (kein muss) die Serviceleistungen wie folgt zu sehen sein: VERKAUF - VERMIETUNG - BERATUNG
Die Farben sollen zu unserem Logo und zu unserer Website passen und harmonieren (Corporate Design) - trotzdem nicht zu schlicht, ein Eye-Catcher darf vorhanden sein.

```html
<!DOCTYPE html>
<html lang="de">
<head>
<meta charset="utf-8">
<title>KORV Immobilien – Plakat</title>
<link href="https://fonts.googleapis.com/css2?family=Poppins:wght@300;700;800&display=swap" rel="stylesheet">
<style>
  :root {
    --gold: #9b8420;
    --gold-light: #a88f24;
    --white: #ffffff;
    --ink: #3a3a3a;
    --band: rgba(22, 26, 18, 0.82);
    --sky-top: #6f8fb4;
    --sky-low: #c3d0dc;
    --grass: #3f5a2a;
    --grass-dark: #1f2d16;
    --suit: #22252b;
  }
  html, body {
    margin: 0;
    padding: 0;
    width: 842px;
    height: 1200px;
    overflow: hidden;
    background: var(--white);
    font-family: "Poppins", sans-serif;
  }
  .poster {
    position: absolute;
    left: 89px;
    top: 167px;
    width: 668px;
    height: 313px;
    overflow: hidden;
  }
  .poster__scene {
    position: absolute;
    inset: 0;
    background:
      linear-gradient(180deg, var(--sky-top) 0%, var(--sky-low) 45%, #8a9a84 58%, var(--grass) 78%, var(--grass-dark) 100%);
  }
  .poster__portrait {
    position: absolute;
    left: 14px;
    top: 16px;
    width: 200px;
    height: 297px;
    border-radius: 90px 90px 0 0;
    background: linear-gradient(180deg, #8a6a4e 0%, #6d5440 35%, var(--suit) 60%, #15171b 100%);
  }
  .poster__band {
    position: absolute;
    inset: 0;
  }
  .brand {
    position: absolute;
    right: 0;
    top: 0;
    width: 227px;
    height: 67px;
    background: var(--white);
    display: flex;
    align-items: center;
    justify-content: center;
    gap: 8px;
  }
  .brand__mark {
    width: 10px;
    height: 10px;
    background: var(--gold);
  }
  .brand__name {
    font-weight: 300;
    font-size: 19px;
    letter-spacing: 0.5px;
    color: var(--ink);
    white-space: nowrap;
  }
  .services {
    position: absolute;
    left: 161px;
    top: 58px;
    width: 114px;
    height: 114px;
    border-radius: 50%;
    background: var(--gold);
    display: flex;
    align-items: center;
    justify-content: center;
  }
  .services::before {
    content: "";
    position: absolute;
    inset: 5px;
    border: 1px solid rgba(255,255,255,0.8);
    border-radius: 50%;
  }
  .services__list {
    margin: 0;
    padding: 0;
    list-style: none;
    transform: rotate(-15deg);
    text-align: center;
    color: var(--white);
    font-weight: 700;
    font-size: 11px;
    line-height: 1.45;
    letter-spacing: 0.3px;
  }
  .headline {
    position: absolute;
    left: 236px;
    top: 200px;
    margin: 0;
    font-weight: 800;
    font-size: 28px;
    line-height: 34px;
    color: var(--white);
  }
  .headline__accent { color: var(--gold-light); }
  .contact {
    position: absolute;
    left: 237px;
    top: 279px;
    display: flex;
    align-items: center;
    gap: 9px;
    font-weight: 700;
    font-size: 13px;
    color: var(--white);
  }
  .contact__web { color: var(--gold-light); }
  .contact__divider {
    width: 1.5px;
    height: 18px;
    background: var(--white);
  }
</style>
</head>
<body>
  <main class="poster">
    <div class="poster__scene" role="img" aria-label="Foto: moderne Villa mit Betonfassade und Holzelementen vor Bäumen, Rasen im Vordergrund, blauer Himmel"></div>
    <div class="poster__portrait" role="img" aria-label="Foto: Immobilienmaklerin im dunklen Blazer mit verschränkten Armen"></div>
    <svg class="poster__band" viewBox="0 0 668 313" width="668" height="313" aria-hidden="true">
      <polygon points="0,195 548,195 604,313 0,313" fill="var(--band)"/>
    </svg>
    <div class="brand">
      <span class="brand__mark"></span>
      <span class="brand__name">KORV IMMOBILIEN</span>
    </div>
    <div class="services">
      <ul class="services__list">
        <li>VERKAUF</li>
        <li>VERMIETUNG</li>
        <li>BERATUNG</li>
      </ul>
    </div>
    <h1 class="headline">Ihr <span class="headline__accent">regionaler</span><br>Immobilienexperte</h1>
    <p class="contact">
      <span class="contact__web">www.korv-immo.at</span>
      <span class="contact__divider"></span>
      <span class="contact__phone">Tel.: 06641357924</span>
    </p>
  </main>
</body>
</html>
```